Tidal Fern Business Cards

We need something new, fun and exciting for business cards. Our current ones are just plain and we need a design that pops. We want name, position held, phone, email on the front, and a 20% discount on the back. I have also uploaded our old business cards creative to see what we are not wanting, and how boring they were and we want something jazzed up from this, cool design and catches people attention.

```html
<!DOCTYPE html>
<html lang="en">
<head>
<meta charset="utf-8">
<title>Tidal Fern Business Cards</title>
<link href="https://fonts.googleapis.com/css2?family=Montserrat:ital,wght@0,400;0,500;0,600;1,400&display=swap" rel="stylesheet">
<style>
  :root {
    --backdrop: #dcbfc1;
    --navy: #173a6e;
    --navy-light: #20508f;
    --coral: #f1706f;
    --coral-soft: #f58a87;
    --white: #ffffff;
    --indigo-deep: #0c0f5a;
    --indigo: #2a2cc4;
    --violet: #4a2bb8;
  }
  * { margin: 0; padding: 0; box-sizing: border-box; }
  html, body {
    width: 1200px; height: 1000px; overflow: hidden;
    background: var(--backdrop);
    font-family: "Montserrat", sans-serif;
  }
  .sheet { position: relative; width: 1200px; height: 1000px; }
  .card {
    position: absolute; top: 320px;
    width: 555px; height: 359px;
    background: var(--white); overflow: hidden;
  }
  .card--front { left: 30px; }
  .card--back { left: 615px; }

  /* Front */
  .front-header {
    position: absolute; left: 0; top: 0; width: 100%; height: 101px;
    display: flex; align-items: center; justify-content: center; gap: 14px;
  }
  .brand-dot { width: 22px; height: 22px; border-radius: 50%; background: var(--coral); }
  .brand-name {
    font-size: 58px; font-weight: 600; color: var(--navy);
    letter-spacing: -1px; line-height: 1;
  }
  .front-panel {
    position: absolute; left: 0; top: 101px; width: 100%; height: 216px;
    background: radial-gradient(ellipse at 35% 40%, var(--navy-light), var(--navy) 70%);
  }
  .leaf-art { position: absolute; }
  .leaf-art--left {
    left: 0; top: 14px; width: 192px; height: 185px;
    background: radial-gradient(ellipse at 50% 60%, rgba(255,255,255,0.28), rgba(255,255,255,0) 70%);
  }
  .leaf-art--right {
    left: 385px; top: 0; width: 170px; height: 216px;
    background: radial-gradient(ellipse at 60% 55%, rgba(241,112,111,0.45), rgba(241,112,111,0) 70%);
  }
  .contact { position: absolute; left: 195px; top: 14px; color: var(--white); }
  .contact-name { font-size: 34px; font-weight: 400; line-height: 1.1; letter-spacing: 0.5px; }
  .contact-name .first { color: var(--coral); }
  .contact-role { font-size: 17px; font-style: italic; margin-top: -1px; }
  .contact-phone { font-size: 19px; margin-top: 25px; letter-spacing: 0.3px; }
  .contact-email { font-size: 19px; margin-top: 24px; letter-spacing: 0.3px; }
  .contact-email .domain { color: var(--coral); }
  .front-footer {
    position: absolute; left: 0; top: 322px; width: 100%; height: 22px;
    background: linear-gradient(90deg, var(--coral-soft), var(--coral));
    color: var(--navy); font-size: 16px; line-height: 22px; padding-left: 8px;
  }

  /* Back */
  .offer-photo {
    position: absolute; left: 0; top: 0; width: 461px; height: 359px;
    background:
      radial-gradient(ellipse at 30% 30%, rgba(74,43,184,0.7), rgba(74,43,184,0) 55%),
      radial-gradient(ellipse at 75% 70%, rgba(42,44,196,0.7), rgba(42,44,196,0) 60%),
      var(--indigo-deep);
  }
  .offer-frame {
    position: absolute; left: 10px; top: 8px; width: 441px; height: 343px;
    border: 2px solid var(--white);
  }
  .offer-text {
    position: absolute; left: 0; top: 0; width: 461px; height: 359px;
    display: flex; flex-direction: column; align-items: center; justify-content: center;
    color: var(--white); font-weight: 400; font-size: 62px; line-height: 1.3;
    letter-spacing: 1px;
  }
  .brand-strip {
    position: absolute; left: 461px; top: 0; width: 94px; height: 359px;
    display: flex; flex-direction: column; align-items: center; padding-top: 22px; gap: 16px;
  }
  .brand-strip .brand-dot { width: 26px; height: 26px; }
  .brand-name--vertical {
    writing-mode: vertical-rl; font-size: 50px; letter-spacing: -1px;
  }
</style>
</head>
<body>
<main class="sheet">
  <section class="card card--front">
    <header class="front-header">
      <span class="brand-dot"></span>
      <span class="brand-name">Tidal Fern</span>
    </header>
    <div class="front-panel">
      <div class="leaf-art leaf-art--left" role="img" aria-label="White line illustration of a fern-like leaf"></div>
      <div class="leaf-art leaf-art--right" role="img" aria-label="Coral line illustration of a fern-like leaf"></div>
      <div class="contact">
        <p class="contact-name"><span class="first">Nora</span> Ellison</p>
        <p class="contact-role">manager</p>
        <p class="contact-phone">720-555-0148</p>
        <p class="contact-email">info<span class="domain">@tidalfern.com</span></p>
      </div>
    </div>
    <footer class="front-footer">medical cannabis</footer>
  </section>

  <section class="card card--back">
    <div class="offer-photo" role="img" aria-label="Photograph of dense leaves in deep blue and violet tones"></div>
    <div class="offer-frame"></div>
    <div class="offer-text">
      <span>20%</span>
      <span>Discount</span>
    </div>
    <aside class="brand-strip">
      <span class="brand-dot"></span>
      <span class="brand-name brand-name--vertical">Tidal Fern</span>
    </aside>
  </section>
</main>
</body>
</html>
```